Copper Lantern: A Self Care Session for Employees

I need a flyer for organizations and businnesses. I am offering a session that will address behavioral issues such as coming to work late, not getting along with others and not working together as a team. I am a life coach who works with difficult employees, helping them address their issues and helping them be a better version of themselves. I also offer a leadership class for managers. I would like the flyer to be professional, clean and convey a feeling of trust. I would prefer to see disgns that use the color blue.

Target Market(s)

small businesses

Industry/Entity Type

Work

Font styles to use
Sans Serif

Colors
34a7d8
85cae6
0792cd
ffffff

Requirements
Must have
• shades of blue and perhaps white. should be clean, fresh and professional
Nice to have
• simple yet warm
Should not have
• distracting and heavy, playful

```html
<!DOCTYPE html>
<html lang="en">
<head>
<meta charset="utf-8">
<title>Copper Lantern: A Self Care Session for Employees</title>
<link href="https://fonts.googleapis.com/css2?family=Roboto:wght@300;400;700;900&family=Roboto+Condensed:wght@300;400;700&display=swap" rel="stylesheet">
<style>
  :root {
    --blue-deep: #2f3fae;
    --blue-mid: #1f6fd0;
    --blue-bright: #0792cd;
    --blue-sky: #34a7d8;
    --blue-pale: #85cae6;
    --white: #ffffff;
    --ink: #0c1a2b;
    --bar-dark: #3b3b3b;
    --bar-light: #676767;
  }
  * { margin: 0; padding: 0; box-sizing: border-box; }
  html, body { width: 927px; height: 1200px; overflow: hidden; background: var(--white); }
  .flyer {
    position: relative; width: 927px; height: 1200px; overflow: hidden;
    background: var(--white); font-family: "Roboto", sans-serif;
  }
  .title-panel {
    position: absolute; left: 51px; top: 0; width: 427px; height: 653px;
    background: linear-gradient(150deg, #2a5fd6 0%, var(--blue-deep) 45%, #2e55c8 70%, var(--blue-mid) 100%);
    overflow: hidden;
  }
  .title-panel svg.facets { position: absolute; inset: 0; }
  .panel-fade {
    position: absolute; left: 51px; top: 653px; width: 427px; height: 120px;
    background: linear-gradient(to bottom, rgba(47,63,174,0.18), rgba(255,255,255,0));
  }
  .brand-box {
    position: absolute; left: 137px; top: 0; width: 149px; height: 183px;
    background: var(--white); display: flex; flex-direction: column;
    align-items: center; justify-content: center; gap: 10px; z-index: 2;
  }
  .brand-dot { width: 34px; height: 34px; border-radius: 50%; background: var(--blue-sky); }
  .brand-name {
    font-family: "Roboto Condensed", sans-serif; font-weight: 700; font-size: 15px;
    color: var(--ink); text-align: center; line-height: 1.15; text-transform: uppercase;
  }
  .title {
    position: absolute; left: 74px; top: 130px; color: var(--white); z-index: 1;
    text-transform: uppercase; line-height: 1;
  }
  .title .light { font-weight: 300; font-size: 62px; display: block; }
  .title .heavy { font-weight: 900; font-size: 82px; display: block; letter-spacing: -1px; }
  .title .a { font-size: 54px; margin-bottom: 6px; }
  .title .self { margin-bottom: 4px; }
  .title .care { margin-bottom: 14px; }
  .title .session { margin-bottom: 8px; }
  .title .for { margin-bottom: 10px; }
  .title .employees { font-size: 58px; font-weight: 700; letter-spacing: 0; }
  .coach-name {
    display: block; margin-top: 20px; font-weight: 300; font-size: 51px;
    color: var(--blue-sky); letter-spacing: 0;
  }
  .pitch {
    position: absolute; left: 522px; top: 116px; width: 380px;
    font-family: "Roboto Condensed", sans-serif; color: var(--ink); text-transform: uppercase;
  }
  .question { font-size: 35px; font-weight: 300; line-height: 1.15; }
  .question strong { font-weight: 700; }
  .question + .question { margin-top: 24px; margin-left: 6px; }
  .help {
    margin-top: 38px; margin-left: 5px; text-transform: none; font-weight: 300;
    font-size: 26px; line-height: 1.35;
  }
  .help .big { font-size: 48px; }
  .audience-photo {
    position: absolute; left: 0; top: 700px; width: 927px; height: 358px;
    background: linear-gradient(to bottom, #ffffff 0%, #e9e6e4 18%, #6d5f55 45%, #2c2a2d 75%, #1f2024 100%);
  }
  .footer-bar { position: absolute; left: 0; top: 1058px; width: 927px; height: 142px; }
  .footer-bar svg { position: absolute; inset: 0; }
  .event-name {
    position: absolute; left: 73px; top: 23px; color: var(--white);
    font-family: "Roboto", sans-serif; text-transform: uppercase; line-height: 1.2;
  }
  .event-name .label { font-size: 21px; display: block; margin-bottom: 4px; }
  .event-name .line { font-size: 28px; display: block; }
  .contact {
    position: absolute; left: 522px; top: 24px; color: var(--white);
    font-family: "Roboto Condensed", sans-serif; font-size: 24px; line-height: 1.4;
  }
  .contact strong { font-weight: 700; }
</style>
</head>
<body>
<div class="flyer">
  <div class="title-panel">
    <svg class="facets" width="427" height="653" viewBox="0 0 427 653" aria-hidden="true">
      <polygon points="0,0 180,0 60,260" fill="#3b7be0" opacity="0.35"/>
      <polygon points="427,40 300,300 427,420" fill="#1c2f9a" opacity="0.5"/>
      <polygon points="200,180 427,120 340,420" fill="#3f8ee6" opacity="0.3"/>
      <polygon points="0,330 220,480 0,620" fill="#4a9ae8" opacity="0.3"/>
      <polygon points="160,653 427,470 427,653" fill="#1f3aa8" opacity="0.45"/>
      <polygon points="90,420 300,560 130,653" fill="#2c6fd8" opacity="0.35"/>
      <polygon points="260,0 427,0 380,160" fill="#4c86e8" opacity="0.3"/>
    </svg>
  </div>
  <div class="panel-fade"></div>

  <div class="brand-box">
    <div class="brand-dot"></div>
    <div class="brand-name">Bright Path<br>Coaching</div>
  </div>

  <h1 class="title">
    <span class="light a">A</span>
    <span class="heavy self">Self</span>
    <span class="heavy care">Care</span>
    <span class="light session">Session</span>
    <span class="light for">For</span>
    <span class="heavy employees">Employees</span>
    <span class="coach-name">Marisol Keane</span>
  </h1>

  <div class="pitch">
    <p class="question">Are your employees bringing <strong>personal issues on the job?</strong></p>
    <p class="question">Is it affecting team <strong>communication</strong> or may be even <strong>productivity?</strong></p>
    <p class="help">If the behavior of an employee,<br>manager or your entire staff<br>is a problem <span class="big">I can help.</span></p>
  </div>

  <div class="audience-photo" role="img" aria-label="Photo of a group of business people seen from behind, looking up"></div>

  <div class="footer-bar">
    <svg width="927" height="142" viewBox="0 0 927 142" aria-hidden="true">
      <rect x="0" y="0" width="927" height="142" fill="var(--bar-light)"/>
      <polygon points="440,0 502,71 440,142 470,142 532,71 470,0" fill="#585858"/>
      <polygon points="0,0 440,0 482,71 440,142 0,142" fill="var(--bar-dark)"/>
    </svg>
    <div class="event-name">
      <span class="label">Copper Lantern:</span>
      <span class="line">A Self Care Session</span>
      <span class="line">For Employees</span>
    </div>
    <div class="contact">
      For more information contact<br>
      Marisol Keane on<br>
      <strong>242-555-0187 or 555-0143</strong>
    </div>
  </div>
</div>
</body>
</html>
```